Used Car Dealer seeks an Amazing Business Card Design

We are looking for a business card design that incorporates our logo and grabs the attention of anyone we give the business card to.

Looking to use the same colors as the logo. Our Logo choice is the black background with Red and Silver/Grey Lettering.

We also would like to see some embossed designs.

Target Market(s)

Used Car Buyers, Automotive, Auto

Industry/Entity Type

Automotive

Contact Information for Business Card

BVEL7K
Gordon Whitlock
482 Tarrow Lane
Suite 207
Calder Falls, OR 97412
Office (770) 555-0142
Cell (770) 555-0187
bvel7kga@quellmail.com
www.bvel7kga.com

Colors
ffffff
ee3036

Requirements
Must have
• Must include our logo (Black Background with Red and Silver/Grey Lettering)
Nice to have
• Embossed Design. Can be Single or Double Sided.

```html
<!DOCTYPE html>
<html lang="en">
<head>
<meta charset="utf-8">
<title>BVEL7K – Gordon Whitlock</title>
<link rel="stylesheet" href="https://fonts.googleapis.com/css2?family=Arimo:wght@700&display=swap">
<style>
  :root {
    --card-bg: #333536;
    --card-bg-deep: #2c2e2f;
    --accent-red: #ff0a0a;
    --accent-edge: #5a0000;
    --text-silver: #b9b9b9;
    --brand-silver: #c9c9c9;
  }
  html, body {
    margin: 0;
    padding: 0;
    width: 1200px;
    height: 686px;
    overflow: hidden;
    background: var(--card-bg);
  }
  .card {
    position: relative;
    width: 1200px;
    height: 686px;
    background: radial-gradient(ellipse at 50% 40%, var(--card-bg) 0%, var(--card-bg-deep) 100%);
    font-family: "Arimo", Arial, sans-serif;
    font-weight: 700;
    color: var(--text-silver);
    overflow: hidden;
  }
  .brand-name {
    position: absolute;
    left: 0;
    width: 100%;
    top: 128px;
    text-align: center;
    font-size: 52px;
    line-height: 60px;
    color: var(--brand-silver);
    letter-spacing: 1px;
  }
  .rule {
    position: absolute;
    height: 9px;
    background: var(--accent-red);
    box-shadow: 0 0 0 1px var(--accent-edge);
  }
  .rule--name-top { left: 415px; width: 371px; top: 230px; }
  .rule--name-bottom { left: 415px; width: 371px; top: 303px; }
  .person-name {
    position: absolute;
    left: 0;
    width: 100%;
    top: 244px;
    text-align: center;
    font-size: 41px;
    line-height: 48px;
  }
  .band {
    position: absolute;
    top: 427px;
    height: 24px;
    background: var(--accent-red);
    box-shadow: 0 0 0 1px var(--accent-edge);
  }
  .band--left { left: 0; width: 371px; }
  .band--middle { left: 415px; width: 371px; }
  .band--right { left: 830px; width: 370px; }
  .contact {
    position: absolute;
    text-align: center;
    font-size: 25px;
    line-height: 43px;
    margin: 0;
  }
  .contact--phones { left: 36px; width: 300px; top: 524px; }
  .contact--address { left: 430px; width: 340px; top: 503px; }
  .contact--web { left: 840px; width: 350px; top: 524px; }
  .contact span { display: block; }
</style>
</head>
<body>
  <div class="card">
    <div class="brand-name">BVEL7K</div>

    <div class="rule rule--name-top"></div>
    <div class="person-name">Gordon Whitlock</div>
    <div class="rule rule--name-bottom"></div>

    <div class="band band--left"></div>
    <div class="band band--middle"></div>
    <div class="band band--right"></div>

    <p class="contact contact--phones">
      <span>(541) 555-0142</span>
      <span>(541) 555-0187</span>
    </p>
    <p class="contact contact--address">
      <span>482 Tarrow Lane</span>
      <span>Suite 207</span>
      <span>Calder Falls, OR 97412</span>
    </p>
    <p class="contact contact--web">
      <span>bvel7kga@quellmail.com</span>
      <span>www.bvel7kga.com</span>
    </p>
  </div>
</body>
</html>
```